New company looking for logo, for business cards and email signature.
we provide Safety, Training and Project Management Services to Mining and Transport sectors.

HALVORN CONSULTANCY, Tom Ashcrove, Principal Consultant, 0491362817, halvornconsultancy@postvale.example , Unit 412,KestwickRidge Business Hub,817 Tulloch Road, Corrabel, 4832.
Sustainable Production through Safety, Training and Leadership.

```html
<!DOCTYPE html>
<html lang="en">
<head>
<meta charset="utf-8">
<title>Halvorn Consultancy – Business Cards</title>
<link rel="stylesheet" href="https://fonts.googleapis.com/css2?family=Arimo:wght@400;700&display=swap">
<style>
  :root {
    --canvas-bg: #e9e8e4;
    --blue-deep: #0d4f8f;
    --blue-mid: #1668ae;
    --blue-light: #3f8fcc;
    --paper: #f7f7f7;
    --white: #ffffff;
  }
  * { box-sizing: border-box; margin: 0; padding: 0; }
  html, body {
    width: 1200px; height: 1023px; overflow: hidden;
    background: var(--canvas-bg);
    font-family: "Arimo", Arial, sans-serif;
  }
  .canvas { position: relative; width: 1200px; height: 1023px; }

  .card {
    position: absolute;
    width: 560px; height: 340px;
    border-radius: 4px;
    overflow: hidden;
    box-shadow: 0 10px 28px rgba(0,0,0,0.22);
  }

  /* Back of card */
  .card-back {
    left: 90px; top: 120px;
    background: linear-gradient(135deg, var(--blue-deep) 0%, var(--blue-mid) 45%, var(--blue-light) 75%, var(--blue-mid) 100%);
    color: var(--white);
    display: flex; flex-direction: column; align-items: center; justify-content: center;
    gap: 26px;
  }
  .back-mark { display: flex; align-items: center; gap: 12px; }
  .back-mark .mark-square { width: 34px; height: 34px; background: var(--white); }
  .back-mark .mark-name { font-weight: 700; font-size: 26px; letter-spacing: 1px; color: var(--white); }
  .tagline { text-align: center; font-size: 19px; line-height: 1.35; color: var(--white); }

  /* Front of card */
  .card-front { left: 550px; top: 590px; background: var(--paper); }
  .front-top {
    height: 150px; padding: 0 40px;
    display: flex; align-items: center; gap: 24px;
  }
  .front-top .mark-circle { width: 92px; height: 92px; border-radius: 50%; background: var(--blue-mid); flex: none; }
  .wordmark { font-weight: 700; color: var(--blue-mid); line-height: 1.05; }
  .wordmark .line-1 { display: block; font-size: 40px; letter-spacing: 1px; }
  .wordmark .line-2 { display: block; font-size: 24px; letter-spacing: 2px; }

  .front-details {
    height: 190px; padding: 22px 36px 0;
    background: linear-gradient(120deg, var(--blue-light) 0%, var(--blue-mid) 40%, var(--blue-deep) 100%);
    color: var(--white); text-align: right;
    font-size: 15px; line-height: 1.4;
  }
  .person-name { font-weight: 700; font-size: 21px; line-height: 1.2; }
  .person-role { margin-bottom: 8px; }
  .contact-line { display: flex; justify-content: flex-end; align-items: center; gap: 6px; }
  .contact-line svg { width: 13px; height: 13px; flex: none; }
</style>
</head>
<body>
<main class="canvas">

  <section class="card card-back" aria-label="Card back">
    <div class="back-mark">
      <span class="mark-square" aria-hidden="true"></span>
      <span class="mark-name">HALVORN</span>
    </div>
    <p class="tagline">Sustainable Production through Safety<br>Training and Leadership.</p>
  </section>

  <section class="card card-front" aria-label="Card front">
    <div class="front-top">
      <span class="mark-circle" aria-hidden="true"></span>
      <h1 class="wordmark"><span class="line-1">HALVORN</span><span class="line-2">CONSULTANCY</span></h1>
    </div>
    <div class="front-details">
      <p class="person-name">Tom Ashcrove</p>
      <p class="person-role">Principal Consultant</p>
      <p class="contact-line">049-136-2817
        <svg viewBox="0 0 16 16" aria-hidden="true"><rect width="16" height="16" rx="2" fill="#fff"/><path d="M5 3.5l1.6 2.4-1 1a6 6 0 0 0 3.5 3.5l1-1 2.4 1.6-1 1.5C8 12.5 3.5 8 4 4.5z" fill="#1668ae"/></svg>
      </p>
      <p class="contact-line">halvornconsultancy@postvale.example
        <svg viewBox="0 0 16 16" aria-hidden="true"><rect width="16" height="16" rx="2" fill="#fff"/><rect x="3" y="5" width="10" height="7" fill="none" stroke="#1668ae" stroke-width="1.3"/><path d="M3 5l5 4 5-4" fill="none" stroke="#1668ae" stroke-width="1.3"/></svg>
      </p>
      <p>Unit 412,KestwickRidge Business Hub</p>
      <p>817 Tulloch Road, Corrabel, 4832</p>
    </div>
  </section>

</main>
</body>
</html>
```